Breakthrough Medical Research company needs Podcast Album Cover

We are launching a podcast called “The Cortex Bloom Sessions Show” with a mission to accelerate breakthroughs in Neuron Regeneration by bringing together the world’s experts in neurodegenerative diseases, spinal cord injury, and artificial intelligence. Design doesn’t need to be monochromatic but we would like it to utilize the color Blue. The design should also incorporate the Title of the podcast large enough to easily read on a small thumbnail on a phone. We’d also like the design to convey the healing or regeneration of a Neuron.

```html
<!DOCTYPE html>
<html lang="en">
<head>
<meta charset="utf-8">
<title>The Cortex Bloom Sessions Show — Podcast Cover</title>
<link rel="stylesheet" href="https://fonts.googleapis.com/css2?family=Lexend:wght@300;700&display=swap">
<style>
  :root {
    --canvas-bg: #eef2f5;
    --teal: #14d2b2;
    --sky: #10a0e2;
    --navy: #033a8f;
    --title-bold: #0c3b92;
    --title-light: #f4f8ff;
    --bar: #ffffff;
    --neuron-lilac: #b8a6e0;
    --neuron-aqua: #33e0e6;
  }
  * { margin: 0; padding: 0; box-sizing: border-box; }
  html, body { width: 1200px; height: 807px; overflow: hidden; }
  body { background: var(--canvas-bg); position: relative; font-family: "Lexend", sans-serif; }

  .cover {
    position: absolute; left: 260px; top: 63px;
    width: 680px; height: 680px;
    background: var(--navy);
    overflow: hidden;
  }
  .cover-shapes { position: absolute; inset: 0; }

  .cover-title {
    position: absolute; left: 20px; right: 20px; top: 34px;
    text-align: center; text-transform: uppercase;
    line-height: 88px; font-size: 60px; letter-spacing: 0;
    white-space: nowrap;
  }
  .cover-title .light { font-weight: 300; color: var(--title-light); }
  .cover-title .bold { font-weight: 700; color: var(--title-bold); }
  .cover-title .line { display: block; }

  .neuron-art {
    position: absolute; left: 36px; top: 390px;
    width: 405px; height: 240px;
    border-radius: 120px;
    background: radial-gradient(ellipse at 30% 50%, var(--neuron-lilac) 0%, rgba(51,224,230,0.55) 45%, rgba(3,58,143,0) 75%);
    opacity: 0.85;
  }
  .sound-wave { position: absolute; left: 455px; top: 449px; }
</style>
</head>
<body>
  <div class="cover">
    <svg class="cover-shapes" width="680" height="680" viewBox="0 0 680 680">
      <defs>
        <linearGradient id="titleBand" x1="0" y1="0" x2="1" y2="0.4">
          <stop offset="0" stop-color="var(--teal)"/>
          <stop offset="1" stop-color="var(--sky)"/>
        </linearGradient>
      </defs>
      <path d="M0 0 H680 V339 H585 L484 398 L499 339 H0 Z" fill="url(#titleBand)"/>
      <path d="M499 339 L484 398 L585 339" fill="none" stroke="#7fe6f0" stroke-width="3" stroke-linejoin="round"/>
    </svg>

    <h1 class="cover-title">
      <span class="line"><span class="light">The </span><span class="bold">Cortex</span></span>
      <span class="line bold">Bloom Sessions</span>
      <span class="line light">Show</span>
    </h1>

    <div class="neuron-art" role="img" aria-label="Illustration of a regenerating neuron: cell body with arcing dendrites and an axon ending in small plus signs"></div>

    <svg class="sound-wave" width="190" height="120" viewBox="0 0 190 120" aria-hidden="true">
      <g stroke="var(--bar)" stroke-width="5" stroke-linecap="round">
        <line x1="4" y1="44" x2="4" y2="76"/>
        <line x1="18" y1="30" x2="18" y2="90"/>
        <line x1="32" y1="14" x2="32" y2="106"/>
        <line x1="46" y1="38" x2="46" y2="82"/>
        <line x1="60" y1="24" x2="60" y2="96"/>
        <line x1="74" y1="46" x2="74" y2="74"/>
        <line x1="88" y1="8" x2="88" y2="112"/>
        <line x1="102" y1="30" x2="102" y2="90"/>
        <line x1="116" y1="42" x2="116" y2="78"/>
        <line x1="130" y1="18" x2="130" y2="102"/>
        <line x1="144" y1="36" x2="144" y2="84"/>
        <line x1="158" y1="26" x2="158" y2="94"/>
        <line x1="172" y1="46" x2="172" y2="74"/>
      </g>
    </svg>
  </div>
</body>
</html>
```